Postcard Design for Licensed Financial Agent

I want a postcard designed to be more like a flyer and a business card combined. This is to draw the attention of individual searching for or have overlooked the need in their lives for life insurance. Right now I am not very sure what size postcard will work best for this project so I selected medium. . I am a licensed agent and I have worked on some ideals of the basics that I would like to have but want your professional input on making this product successfully. My business cards were created by Prontomark and I would like to have that information on the back of the postcard.

On one side I want the information from the attachment from the insurance interest postcard document that I attempted to create.

On the other side of the postcard I would like the information from my business card you printed for me on August 28 of 2014. The box number reads K 47315820461538 K72 at the bottom of the bar code it has TM83. If there is any other information you need to get the business card information you printed for me previously please contact me with any questions so we together can get this project on its way. Thank you for your attention to this matter. Ilsa Marwood

Industry/Entity Type

Business

Requirements
Must have
• Text for front: IF YOU EXPERIENCED THE SUDDEN LOST OF A LOVED ONE CAN YOU IMMEDIATELY PROVIDE THE COST OF FINAL EXPENSE?*

```html
<!DOCTYPE html>
<html lang="en">
<head>
<meta charset="utf-8">
<title>Ilsa Marwood – Licensed Agent Postcard</title>
<link rel="stylesheet" href="https://fonts.googleapis.com/css2?family=Arimo:ital,wght@0,400;0,700;1,400;1,700&family=Oswald:wght@400;600&display=swap">
<style>
  :root {
    --backdrop: #6b6c6f;
    --card: #ffffff;
    --navy: #113a5c;
    --sky: #3f97d8;
    --name: #1b4a74;
    --ink: #111111;
    --teal-dot: #5fc9c8;
    --stamp: #e6e6e6;
    --rule: #cfcfcf;
    --brand: #1f7cc4;
  }
  * { margin: 0; padding: 0; box-sizing: border-box; }
  html, body {
    width: 1200px; height: 992px; overflow: hidden;
    background: var(--backdrop);
  }
  .postcard {
    position: absolute; left: 73px; top: 157px;
    width: 1054px; height: 678px;
    background: var(--card);
    overflow: hidden;
    font-family: "Arimo", Arial, sans-serif;
    box-shadow: 0 10px 18px rgba(0,0,0,.35);
  }
  .postcard__shapes { position: absolute; inset: 0; }
  .agent-photo {
    position: absolute; left: 24px; top: 24px; width: 160px; height: 178px;
    background: #fff; padding: 5px; border-radius: 4px;
  }
  .agent-photo__fill {
    width: 100%; height: 100%;
    background: linear-gradient(160deg, #a89a86 0%, #7a5140 45%, #e9774a 100%);
  }
  .agent-id { position: absolute; left: 211px; top: 44px; color: var(--ink); }
  .agent-id__name { font-size: 29px; font-weight: 700; color: var(--name); letter-spacing: .5px; line-height: 1.1; }
  .agent-id__title { font-size: 23px; font-weight: 700; font-style: italic; line-height: 1.2; }
  .agent-id__address { font-size: 19px; line-height: 1.2; margin-top: 4px; }
  .contact { position: absolute; left: 42px; top: 230px; color: #fff; }
  .contact__phone { display: flex; align-items: center; gap: 10px; font-size: 38px; font-weight: 700; margin-left: 20px; }
  .contact__email { font-size: 27px; margin-top: 6px; }
  .specialties { position: absolute; left: 53px; top: 342px; color: #fff; }
  .specialties__heading { font-size: 24px; font-weight: 400; letter-spacing: .3px; }
  .specialties__list { list-style: none; margin-top: 6px; margin-left: 18px; }
  .specialties__list li {
    position: relative; padding-left: 22px;
    font-size: 25px; font-style: italic; line-height: 1.28;
  }
  .specialties__list li::before {
    content: ""; position: absolute; left: 0; top: 12px;
    width: 10px; height: 10px; border-radius: 50%; background: var(--teal-dot);
  }
  .quote-badge {
    position: absolute; left: 406px; top: 126px; width: 200px; height: 200px;
    display: flex; flex-direction: column; align-items: center; justify-content: center;
    color: #fff; text-align: center; font-family: "Oswald", "Arial Narrow", sans-serif;
  }
  .quote-badge__lead { font-size: 16px; line-height: 1.15; font-weight: 400; }
  .quote-badge__call { font-size: 34px; line-height: 1.05; font-weight: 600; margin-top: 6px; }
  .stamp-box { position: absolute; left: 863px; top: 40px; width: 148px; height: 142px; background: var(--stamp); }
  .address-line { position: absolute; left: 578px; width: 424px; height: 2px; background: var(--rule); }
  .brand-name {
    position: absolute; right: 39px; top: 586px;
    font-size: 43px; font-weight: 400; color: var(--brand); letter-spacing: .3px;
  }
</style>
</head>
<body>
  <div class="postcard">
    <svg class="postcard__shapes" viewBox="0 0 1054 678" width="1054" height="678" aria-hidden="true">
      <path d="M0,174 L470,174 C492,330 420,540 110,678 L0,678 Z" fill="var(--navy)"/>
      <path d="M474,0 L518,0 C562,250 470,520 190,678 L112,678 C420,530 502,300 474,0 Z" fill="var(--sky)"/>
      <circle cx="506" cy="226" r="100" fill="var(--sky)"/>
      <circle cx="506" cy="226" r="90" fill="var(--navy)"/>
    </svg>

    <div class="agent-photo"><div class="agent-photo__fill" role="img" aria-label="Portrait photo of the agent"></div></div>

    <div class="agent-id">
      <p class="agent-id__name">ILSA MARWOOD</p>
      <p class="agent-id__title">Licensed Agent</p>
      <p class="agent-id__address">PO Box 83<br>Brookhaven, NJ 08317</p>
    </div>

    <div class="contact">
      <p class="contact__phone">
        <svg width="36" height="36" viewBox="0 0 36 36" aria-hidden="true">
          <rect x="2" y="2" width="32" height="32" rx="7" fill="none" stroke="#fff" stroke-width="3"/>
          <path d="M13 9c-2 0-3 2-3 4 0 7 6 14 13 14 2 0 4-1 4-3l-4-3-2 2c-3-1-6-4-7-7l2-2z" fill="#fff"/>
        </svg>
        609-555-0148
      </p>
      <p class="contact__email">ms.ilsa.marwood@mailbox.com</p>
    </div>

    <div class="specialties">
      <p class="specialties__heading">SPECIALIZING IN</p>
      <ul class="specialties__list">
        <li>Life Insurance</li>
        <li>Mortgage Protection</li>
        <li>Final Expense &amp;</li>
        <li>Tax Fee Retirement<br>Solutions</li>
      </ul>
    </div>

    <div class="quote-badge">
      <p class="quote-badge__lead">CONTACT YOUR<br>LICENSED AGENT</p>
      <p class="quote-badge__call">TODAY FOR<br>A QUOTE</p>
    </div>

    <div class="stamp-box"></div>
    <div class="address-line" style="top:376px"></div>
    <div class="address-line" style="top:458px"></div>
    <div class="address-line" style="top:540px"></div>

    <p class="brand-name">Kinward Life</p>
  </div>
</body>
</html>
```